Looking for a modern, Professional business card design

We have a simple business card, but are looking for a more modern, professional look. A sample of the basic card is attached as well as the logo. We would also like to add that we offer:
Struggling with your finances?
- Learn to become debt free
- Discover the power of cash
- Control your money instead of it controlling you
Let us help you achieve a new level of financial freedom!
Also, we would like to have a "SPECIAL OFFER!: FREE 30 minute consultation"
Financial Planning

```html
<!DOCTYPE html>
<html lang="en">
<head>
<meta charset="utf-8">
<title>Clearpath Money Coaching – Business Card</title>
<link rel="stylesheet" href="https://fonts.googleapis.com/css2?family=Source+Sans+3:ital,wght@0,400;0,600;0,700;1,700&display=swap">
<style>
  :root {
    --page-bg: #efefed;
    --green-light: #8dc63f;
    --green-mid: #62b233;
    --green-deep: #3f9a2d;
    --green-text: #4a9e2f;
    --white: #ffffff;
    --ink-soft: rgba(255,255,255,0.95);
  }
  * { box-sizing: border-box; margin: 0; padding: 0; }
  html, body {
    width: 1200px; height: 900px; overflow: hidden;
    background: var(--page-bg);
    font-family: "Source Sans 3", "Myriad Pro", Arial, sans-serif;
  }
  .canvas { position: relative; width: 1200px; height: 900px; }

  .card {
    position: absolute; overflow: hidden; border-radius: 14px;
    box-shadow: 0 6px 18px rgba(0,0,0,0.18);
    background: linear-gradient(160deg, var(--green-light) 0%, var(--green-mid) 55%, var(--green-deep) 100%);
    color: var(--white);
  }

  /* Front */
  .card-front { left: 447px; top: 63px; width: 588px; height: 365px; }
  .front-header {
    position: absolute; left: 0; top: 0; width: 100%; height: 94px;
    display: flex; align-items: center; justify-content: center; gap: 10px;
    padding-left: 60px;
  }
  .holder-name { font-size: 22px; font-weight: 700; }
  .name-divider { width: 1.5px; height: 22px; background: var(--white); }
  .holder-title { font-size: 17px; font-weight: 400; }
  .brand-band {
    position: absolute; left: 0; top: 94px; width: 100%; height: 148px;
    background: var(--white);
    display: flex; align-items: center; justify-content: center; gap: 14px;
  }
  .brand-dot { width: 30px; height: 30px; border-radius: 50%; background: var(--green-mid); }
  .brand-name {
    font-size: 34px; font-weight: 700; color: var(--green-deep);
    letter-spacing: 0.5px;
  }
  .contact-block {
    position: absolute; left: 0; top: 242px; width: 100%; height: 123px;
    display: flex; flex-direction: column; align-items: center; justify-content: center;
    padding-left: 60px; padding-bottom: 10px;
    font-size: 16px; line-height: 23px; color: var(--ink-soft);
  }

  /* Back */
  .card-back { left: 203px; top: 478px; width: 566px; height: 348px; }
  .pitch {
    position: absolute; left: 0; top: 0; width: 100%; height: 280px;
    text-align: center; padding-left: 60px;
  }
  .pitch-heading {
    margin-top: 48px; font-size: 20px; font-weight: 700;
    text-decoration: underline; text-underline-offset: 3px;
  }
  .pitch-list { list-style: none; margin-top: 22px; font-size: 16px; line-height: 24px; }
  .pitch-closing {
    margin-top: 36px; font-size: 16px; font-weight: 700; font-style: italic; line-height: 23px;
    padding-right: 60px;
  }
  .offer-band {
    position: absolute; left: 0; top: 280px; width: 100%; height: 47px;
    background: var(--white);
    display: flex; align-items: center; justify-content: center;
    font-size: 17px; font-weight: 600; color: var(--green-text);
  }
  .offer-band strong { font-weight: 700; margin-right: 6px; }
</style>
</head>
<body>
<main class="canvas">
  <section class="card card-front" aria-label="Business card front">
    <header class="front-header">
      <span class="holder-name">Daniel R. Hale</span>
      <span class="name-divider"></span>
      <span class="holder-title">Personal Financial Coach</span>
    </header>
    <div class="brand-band">
      <span class="brand-dot"></span>
      <span class="brand-name">Clearpath Money Coaching</span>
    </div>
    <address class="contact-block" style="font-style:normal">
      <span>(205) 555-0187</span>
      <span>daniel@clearpathmoneycoach.com</span>
      <span>www.clearpathmoneycoach.com</span>
    </address>
  </section>

  <section class="card card-back" aria-label="Business card back">
    <div class="pitch">
      <h2 class="pitch-heading">Struggling with your finances?</h2>
      <ul class="pitch-list">
        <li>Learn to become debt free</li>
        <li>Discover the power of cash</li>
        <li>Control your money instead of it controlling you</li>
      </ul>
      <p class="pitch-closing">Let us help you achieve a new<br>level of financial freedom!</p>
    </div>
    <div class="offer-band"><strong>SPECIAL OFFER!:</strong> FREE 30 minute consultation</div>
  </section>
</main>
</body>
</html>
```